Psychologist website

Simple psychologist website
Site map:
home
self-test
common conditions
children
contact
about
info

Current website:
http://www.moriklepsychology.com.au/

Not in love with logo, or colours etc - open brief
Happy for new font/style/logo for company name

Customer wants clean, credible and warm and friendly look & feel
stock photos OK

Brief:

One home page - simple with 2 or 3 small areas to tease and attract the user and one template page to suit all the other pages

Pages structurally similar to
http://www.quellbyhouse.com.au/
In that the home page is different and the other pages are based on one template

Requirements
Must have
• 2 pages - one home page and one template page
• navigation for site map

```html
<!DOCTYPE html>
<html lang="en">
<head>
<meta charset="utf-8">
<title>Morikle &amp; Associates – Clinical Psychologists</title>
<link rel="stylesheet" href="https://fonts.googleapis.com/css2?family=Arimo:ital,wght@0,400;0,700;1,700&display=swap">
<style>
  :root {
    --sky: #a7d4d8;
    --cream: #f2f1ea;
    --white: #ffffff;
    --teal: #1f7480;
    --teal-bright: #3a9bb0;
    --logo-blue: #2c6d92;
    --ink: #222222;
    --body: #333333;
    --muted: #8a8a8a;
    --rule: #d4d3cc;
    --ph-warm: #c9a98d;
    --ph-blue: #6f8aa4;
    --ph-gym: #b9966a;
    --ph-skin: #d9b49c;
  }
  * { box-sizing: border-box; margin: 0; padding: 0; }
  html, body { width: 1159px; height: 1200px; overflow: hidden; }
  body {
    position: relative;
    font-family: "Arimo", Arial, sans-serif;
    color: var(--body);
    background: linear-gradient(to bottom, var(--sky) 0px, #cfe3df 300px, var(--cream) 560px, var(--cream) 100%);
  }
  .abs { position: absolute; }

  /* header */
  .masthead { left: 93px; top: 24px; width: 966px; height: 457px; background: var(--white); }
  .masthead-rule { left: 93px; top: 112px; width: 966px; height: 1px; background: #bfe0e3; }
  .brand { left: 103px; top: 42px; width: 303px; text-align: right; color: var(--logo-blue); font-weight: 400; }
  .brand-name { font-size: 22px; letter-spacing: 1px; text-transform: uppercase; line-height: 26px; }
  .brand-rule { height: 2px; background: #9cc4da; margin: 4px 0 3px; }
  .brand-tag { font-size: 14px; letter-spacing: 2.6px; text-transform: uppercase; line-height: 18px; }

  .main-nav { right: 116px; top: 68px; display: flex; gap: 17px; font-size: 12px; font-weight: 700; color: var(--ink); white-space: nowrap; }
  .main-nav a { color: inherit; text-decoration: none; letter-spacing: .2px; }
  .main-nav a.current { color: var(--teal-bright); }

  .hero { left: 104px; top: 120px; width: 944px; height: 352px;
    background: linear-gradient(100deg, #5b4a40 0%, var(--ph-warm) 35%, #e6ddd3 60%, #7b5a43 82%, #3e3028 100%); }
  .slider-dots { left: 831px; top: 448px; display: flex; gap: 4px; }
  .slider-dots span { width: 36px; height: 4px; background: var(--white); }

  /* welcome */
  .welcome-photo { left: 105px; top: 516px; width: 156px; height: 146px; border: 3px solid var(--white);
    background: linear-gradient(120deg, #dfe9ee, var(--ph-skin) 55%, #8fb3cd); }
  h2 { font-size: 15px; font-weight: 400; color: var(--teal); text-transform: uppercase; letter-spacing: .3px; }
  .welcome-title { left: 276px; top: 515px; }
  .welcome-lead { left: 278px; top: 543px; width: 510px; font-size: 11.7px; font-weight: 700; line-height: 18.4px; color: var(--body); }
  .welcome-body { left: 277px; top: 607px; width: 525px; font-size: 11.5px; line-height: 18.4px; color: var(--body); }
  .welcome-body b { color: var(--ink); }

  .services-title { left: 818px; top: 515px; }
  .services-list { left: 832px; top: 545px; list-style: none; font-size: 12.5px; line-height: 18.4px; color: var(--ink); letter-spacing: .3px; }
  .services-list .more { color: var(--teal-bright); font-weight: 700; letter-spacing: 0; }

  .section-rule { left: 93px; top: 687px; width: 966px; height: 1px; background: var(--rule); }

  /* feature columns */
  .feature { width: 300px; }
  .feature h2 { margin-bottom: 9px; }
  .feature-img { height: 131px; border: 3px solid var(--white); }
  .feature p { margin-top: 12px; font-size: 11.5px; line-height: 16.4px; color: var(--body); }
  .feature .read { display: block; color: var(--teal); font-weight: 700; }
  .f1 { left: 110px; top: 704px; }
  .f2 { left: 431px; top: 704px; }
  .f3 { left: 762px; top: 704px; }
  .f1 .feature-img { width: 286px; background: linear-gradient(160deg, #4c463d, var(--ph-gym) 55%, #e3c690); }
  .f2 .feature-img { width: 285px; background: linear-gradient(120deg, #57606a, var(--ph-blue) 50%, #3b5675); }
  .f3 .feature-img { width: 286px; height: 136px; margin-top: -5px; background: linear-gradient(100deg, #f4f2f0, var(--ph-skin) 40%, #b4865e 70%, #f0ece8); }

  /* tagline */
  .tagline { left: 114px; top: 981px; width: 913px; height: 93px; border: 3px solid var(--white);
    background: linear-gradient(to bottom, #f7f7f3, #ecebe3); display: flex; align-items: center; justify-content: center; }
  .tagline p { font-size: 16.6px; font-style: italic; font-weight: 700; color: var(--teal); text-align: center; line-height: 21.5px; }

  /* footer */
  .footer-rule { left: 93px; top: 1103px; width: 966px; height: 2px; background: #dcdbd4; }
  .legal { left: 119px; top: 1122px; font-size: 11.5px; line-height: 14px; color: var(--muted); }
  .legal a { color: inherit; text-decoration: none; }
  .social { left: 887px; top: 1120px; }
</style>
</head>
<body>
  <div class="abs masthead"></div>
  <div class="abs masthead-rule"></div>

  <div class="abs brand">
    <div class="brand-name">Morikle &amp; Associates</div>
    <div class="brand-rule"></div>
    <div class="brand-tag">Clinical Psychologists</div>
  </div>

  <nav class="abs main-nav">
    <a class="current" href="#">HOME</a>
    <a href="#">SELF-TEST</a>
    <a href="#">COMMON CONDITIONS</a>
    <a href="#">CHILDREN</a>
    <a href="#">ABOUT</a>
    <a href="#">INFO</a>
    <a href="#">CONTACT</a>
  </nav>

  <div class="abs hero" role="img" aria-label="Photo of a client talking with a psychologist in a bright consulting room"></div>
  <div class="abs slider-dots"><span></span><span></span><span></span><span></span><span></span></div>

  <div class="abs welcome-photo" role="img" aria-label="Photo of a smiling young man"></div>
  <h2 class="abs welcome-title">Welcome to our clinic</h2>
  <p class="abs welcome-lead">Specialising in cognitive-behaviour therapy (CBT) for adults experiencing difficulties with depression, anxiety, eating disorders, stress, trauma, adjustment to illness or disability, and other common issues.</p>
  <p class="abs welcome-body">Our psychologists provide a comfortable, supportive, and confidential environment for their clients. Our first goal is for you to feel comfortable in exploring issues and sharing sharing your concerns, knowing that you have been heard and understood. <b>Read more..</b></p>

  <h2 class="abs services-title">Our services</h2>
  <ul class="abs services-list">
    <li>MOOD</li>
    <li>TRAUMA</li>
    <li>ANXIETY</li>
    <li>ADDICTIONS</li>
    <li>PHYSICAL HEALTH</li>
    <li class="more">and more..</li>
  </ul>

  <div class="abs section-rule"></div>

  <section class="abs feature f1">
    <h2>Physical health</h2>
    <div class="feature-img" role="img" aria-label="Photo of a physiotherapist helping a woman exercise in a gym"></div>
    <p>Sed ut perspiciatis unde omnis iste natus error sit tatem accusantium doloremque laudantium, totam rem eaque atae vitae dicta sunt explicabo. Nemo enim.<a class="read">Read more..</a></p>
  </section>

  <section class="abs feature f2">
    <h2>Trauma</h2>
    <div class="feature-img" role="img" aria-label="Photo of a medical team treating a patient in an emergency room"></div>
    <p>Sed ut perspiciatis unde omnis iste natus error sit tatem accusantium doloremque laudantium, totam rem eaque eatae vitae dicta sunt explicabo. Nemo enim.<a class="read">Read more..</a></p>
  </section>

  <section class="abs feature f3">
    <h2>Anxiety</h2>
    <div class="feature-img" role="img" aria-label="Photo of a worried young woman comforted by a friend"></div>
    <p>Sed ut perspiciatis unde omnis iste natus error sit tatem accusantium doloremque laudantium, totam rem eaque eatae vitae dicta sunt explicabo. Nemo enim.<a class="read">Read more..</a></p>
  </section>

  <div class="abs tagline">
    <p>Clinical psychologists, in Sydney, Chatswood, and Westmead, providing cognitive-behaviour<br>therapy (CBT), treatment, and counselling, for depression, anxiety and other issues</p>
  </div>

  <div class="abs footer-rule"></div>
  <div class="abs legal">
    Copyright 2013. All rights reserved.<br>
    <a href="#">Terms &amp; Conditions</a> &nbsp;-&nbsp;&nbsp; <a href="#">Privacy</a> &nbsp;&nbsp;-&nbsp;&nbsp;&nbsp; <a href="#">Disclaimer</a>
  </div>
  <svg class="abs social" width="150" height="36" viewBox="0 0 150 36" aria-label="Social links">
    <g fill="#e4e4e1" stroke="#9a9a98" stroke-width="2">
      <circle cx="18" cy="18" r="16"/>
      <circle cx="55" cy="18" r="16"/>
      <circle cx="92" cy="18" r="16"/>
      <circle cx="130" cy="18" r="16"/>
    </g>
  </svg>
</body>
</html>
```